Marcus Pellow Carpentry & Joinery

Hello, I would like a flyer designed for my new business doing small projects in my local area for home-owners. I am a professional tradesman.
The type of work I am offering is:
- decks/decking
- external stairs & railings
- install windows & doors
- roofs & gutters
- small additions
- built-in wardrobes
- finish work
- demolition

It would be great if the flyer could mention these, or use phrasing that fits this kind of construction work.
My idea for a slogan was "new work and repairs to any age home".

Please also mention FREE QUOTES and have my email and phone number included on the flyer, along with my carpentry licence number, which I can provided.

I'd like a one page, single-sided flyer that could be printed as DL.
Colour and style is up to you! I'll be placing this flyer on counters & in the windows of local businesses, so something simple and eye-catching is preferred.

Thank you!

```html
<!DOCTYPE html>
<html lang="en">
<head>
<meta charset="utf-8">
<title>Marcus Pellow Carpentry &amp; Joinery – Flyer</title>
<link href="https://fonts.googleapis.com/css2?family=Open+Sans:ital,wght@0,300;0,600;0,700;1,600&family=PT+Sans+Narrow:wght@400;700&display=swap" rel="stylesheet">
<style>
  :root {
    --page-bg: #ece4d8;
    --paper: #ffffff;
    --brown-dark: #3b2a1a;
    --tan: #e6c595;
    --tan-deep: #c9a06c;
    --teal: #4a8081;
    --wood-light: #e9c79a;
    --wood-mid: #d8ad78;
    --deck-red: #8a4a2c;
    --deck-shade: #5b3320;
    --garden: #5d7a3a;
    --tag: #a77a4c;
    --white: #ffffff;
  }
  * { margin: 0; padding: 0; box-sizing: border-box; }
  html, body { width: 684px; height: 1200px; overflow: hidden; }
  body { background: var(--page-bg); position: relative; font-family: "Open Sans", Arial, sans-serif; }

  .flyer {
    position: absolute; left: 80px; top: 77px; width: 506px; height: 1062px;
    background: var(--paper);
    box-shadow: 2px 4px 8px rgba(0,0,0,0.25);
    overflow: hidden;
  }

  .hero {
    position: absolute; left: 0; top: 0; width: 506px; height: 338px;
    background: linear-gradient(180deg, var(--garden) 0%, #7b6a45 28%, var(--deck-red) 45%, #9a5634 70%, var(--deck-shade) 100%);
  }
  .business-name {
    position: absolute; left: 16px; top: 199px;
    font-family: "Open Sans", Arial, sans-serif; font-style: italic; font-weight: 600;
    font-size: 42px; line-height: 56px; color: var(--tan);
    white-space: nowrap;
    text-shadow: 1px 1px 2px rgba(0,0,0,0.35);
  }

  .slogan-band {
    position: absolute; left: 0; top: 348px; width: 506px; height: 63px;
    background: var(--brown-dark);
    display: flex; align-items: center; justify-content: center;
    color: var(--white); font-style: italic; font-weight: 600; font-size: 24px;
    white-space: nowrap;
  }

  .services-panel {
    position: absolute; left: 0; top: 420px; width: 506px; height: 570px;
    background: var(--teal);
  }
  .wood-strip {
    position: absolute; left: 0; top: 0; width: 168px; height: 100%;
    background: linear-gradient(90deg, var(--wood-mid) 0%, var(--wood-light) 45%, var(--wood-mid) 100%);
  }
  .service-photo {
    position: absolute; left: 37px; width: 170px; height: 115px;
    border: 3px solid var(--white);
  }
  .photo-stairs { top: 36px; background: linear-gradient(180deg, #6fa0d6 0%, #b98a68 55%, #6f9a48 100%); }
  .photo-gutter { top: 170px; background: linear-gradient(160deg, #3a74c4 0%, #8fb4e0 50%, #e4e8ec 100%); }
  .photo-window { top: 304px; background: linear-gradient(90deg, #5b4634 0%, #c6a47a 50%, #8a6a48 100%); }
  .photo-wardrobe { top: 434px; background: linear-gradient(180deg, #7a5634 0%, #c89a62 55%, #5a3a22 100%); }

  .offer-list {
    position: absolute; left: 223px; top: 57px; list-style: none;
    font-family: "PT Sans Narrow", "Arial Narrow", sans-serif; font-size: 28px;
    color: var(--white); line-height: 40px; white-space: nowrap;
  }
  .offer-list .offer-heading { font-size: 26px; }
  .offer-list .item::before { content: "\2022"; margin-right: 6px; }

  .call-line {
    position: absolute; left: 218px; top: 450px;
    font-family: "Open Sans", Arial, sans-serif; font-weight: 300;
    font-size: 32px; line-height: 38px; color: var(--tan);
  }

  .quote-tag {
    position: absolute; left: 382px; top: 427px; width: 86px; height: 86px;
    background: var(--tag); transform: rotate(-16deg);
    box-shadow: 2px 3px 5px rgba(0,0,0,0.3);
    display: flex; align-items: center; justify-content: center; text-align: center;
    color: var(--white); font-weight: 700; font-size: 11.5px; line-height: 15px;
  }
  .tag-pin { position: absolute; left: 406px; top: 413px; }

  .footer-band {
    position: absolute; left: 0; top: 998px; width: 506px; height: 64px;
    background: var(--brown-dark); color: var(--tan-deep);
  }
  .footer-phone-icon { position: absolute; left: 17px; top: 14px; }
  .footer-phone {
    position: absolute; left: 73px; top: 12px;
    font-weight: 700; font-size: 26px; line-height: 36px; color: var(--tan);
  }
  .footer-details {
    position: absolute; right: 12px; top: 8px; text-align: right;
    font-weight: 600; font-size: 18px; line-height: 24px; color: var(--tan);
    white-space: nowrap;
  }
</style>
</head>
<body>
  <main class="flyer">
    <section class="hero" role="img" aria-label="Photo of a newly built timber deck with railings and steps beside a brick house"></section>
    <h1 class="business-name">Marcus Pellow<br>Carpentry &amp; Joinery</h1>

    <div class="slogan-band">New Work And Repairs To Any Age Home</div>

    <section class="services-panel">
      <div class="wood-strip"></div>
      <div class="service-photo photo-stairs" role="img" aria-label="Photo of external timber stairs and railings"></div>
      <div class="service-photo photo-gutter" role="img" aria-label="Photo of a tradesman fitting roof gutters"></div>
      <div class="service-photo photo-window" role="img" aria-label="Photo of a tradesman installing a window frame"></div>
      <div class="service-photo photo-wardrobe" role="img" aria-label="Photo of built-in timber wardrobes"></div>

      <ul class="offer-list">
        <li class="offer-heading">We Offer:</li>
        <li class="item">Decks/decking</li>
        <li class="item">External Stairs &amp; Railings</li>
        <li class="item">Install Windows &amp; Doors</li>
        <li class="item">Roofs &amp; Gutters</li>
        <li class="item">Small Additions</li>
        <li class="item">Built-in Wardrobes</li>
        <li class="item">Finish Work</li>
        <li class="item">Demolition</li>
      </ul>

      <p class="call-line">Just<br>call us.</p>

      <svg class="tag-pin" width="14" height="22" viewBox="0 0 14 22" aria-hidden="true">
        <rect x="3" y="0" width="8" height="3" fill="#222"/>
        <rect x="4.5" y="3" width="5" height="8" fill="#333"/>
        <rect x="1" y="11" width="12" height="3" fill="#222"/>
        <line x1="7" y1="14" x2="7" y2="22" stroke="#666" stroke-width="1.5"/>
      </svg>
      <div class="quote-tag">FREE NO<br>OBLIGATION<br>QUOTE</div>
    </section>

    <footer class="footer-band">
      <svg class="footer-phone-icon" width="48" height="36" viewBox="0 0 48 36" aria-hidden="true">
        <path d="M4 12 C4 3 44 3 44 12 L44 15 L34 15 L34 10 L14 10 L14 15 L4 15 Z" fill="#c9a06c"/>
        <path d="M12 14 L36 14 L42 34 L6 34 Z" fill="#c9a06c"/>
        <circle cx="24" cy="24" r="6" fill="#3b2a1a"/>
        <circle cx="24" cy="24" r="2.5" fill="#c9a06c"/>
      </svg>
      <div class="footer-phone">0123456789</div>
      <div class="footer-details">
        <div>licence no. 00000000</div>
        <div>office@pellowjoinery.com</div>
      </div>
    </footer>
  </main>
</body>
</html>
```